Redesign of an insurance website

Attached is an insurance website that I need to redesign. Currently the website is too dark. I like for example www.brenvalo.com . Could you make the website lighter and change the structure a little so that it is more user friendly?

Industry/Entity Type

Insurance

Number of Pages Required

4 page

```html
<!DOCTYPE html>
<html lang="cs">
<head>
<meta charset="utf-8">
<title>Pojistkovo.cz – srovnání pojištění</title>
<link rel="stylesheet" href="https://fonts.googleapis.com/css2?family=Poppins:wght@300;400;500;600;700&family=Open+Sans:wght@300;400&family=Rubik:wght@500;700&display=swap">
<style>
:root{
  --blue:#1f7cf2;
  --orange:#ff7d12;
  --ink:#222;
  --muted:#7a7a7a;
  --line:#e3e3e3;
  --tile:#eef3fa;
  --white:#fff;
}
*{box-sizing:border-box;margin:0;padding:0}
html,body{width:917px;height:1200px;overflow:hidden;background:var(--white)}
body{position:relative;font-family:'Poppins',sans-serif;color:var(--ink)}
a{color:inherit;text-decoration:none}

/* header */
.site-header{position:absolute;left:0;top:0;width:917px;height:61px;background:var(--white)}
.brand{position:absolute;left:114px;top:20px;font:700 19px/1 'Poppins',sans-serif;color:var(--blue);letter-spacing:.5px}
.main-nav a{position:absolute;top:27px;font-size:8.5px;letter-spacing:.6px;color:var(--blue)}
.main-nav a.active{font-weight:600}
.pill{position:absolute;display:flex;align-items:center;justify-content:center;border-radius:12px;color:#fff;font:600 9px/1 'Poppins',sans-serif;letter-spacing:.4px}
.pill.orange{background:var(--orange)}
.pill.blue{background:var(--blue)}

/* hero */
.hero{position:absolute;left:0;top:61px;width:917px;height:449px;
  background:linear-gradient(180deg,#9fd0ee 0%,#5fb9da 100%)}
.social-rail{position:absolute;left:0;top:230px;width:42px;height:134px;background:var(--white);border-right:2px solid var(--orange);display:flex;flex-direction:column;align-items:center;justify-content:space-around;padding:8px 0}
.social-rail span{width:26px;height:26px;background:var(--blue);border-radius:3px}

.quote-card{position:absolute;left:315px;top:142px;width:286px;height:288px;background:var(--white);box-shadow:0 2px 8px rgba(0,0,0,.18)}
.tabs{display:flex;height:38px;border-bottom:1px solid var(--line)}
.tabs span{flex:1;display:flex;align-items:center;justify-content:center;font-size:8.5px;letter-spacing:1.2px;color:#333}
.tabs span.active{font-weight:600;border-bottom:2px solid var(--blue)}
.quote-title{position:absolute;left:0;width:100%;top:56px;text-align:center;font-size:17px;font-weight:400}
.quote-sub{position:absolute;left:0;width:100%;top:97px;text-align:center;font-size:8px}
.products{position:absolute;left:0;top:119px;width:100%;height:70px}
.product{position:absolute;top:0;width:44px;text-align:center}
.product .ring{width:44px;height:44px;border-radius:50%;border:1.5px solid var(--orange);display:flex;align-items:center;justify-content:center}
.product.selected .ring{background:var(--blue);border-color:var(--blue);width:50px;height:50px;margin:-3px}
.product .label{display:block;margin-top:10px;font-size:6.5px;color:var(--orange)}
.product.selected .label{color:var(--blue);margin-top:7px}
.arrow{position:absolute;top:14px}
.zip{position:absolute;left:39px;top:200px;width:208px;height:30px;border:1px solid #cfcfcf;border-radius:2px;display:flex}
.zip .field{flex:1;display:flex;align-items:center;gap:6px;padding-left:8px;font-size:8px;color:#999}
.zip .go{width:74px;background:var(--orange);color:#fff;font-size:8.5px;display:flex;align-items:center;justify-content:center;margin:-1px -1px -1px 0}
.saved{position:absolute;left:0;width:100%;top:238px;text-align:center;font-size:8.5px;color:var(--blue)}

/* why */
.why-title{position:absolute;left:0;width:917px;top:536px;text-align:center;font-size:20px;font-weight:300;color:var(--muted);letter-spacing:.3px}
.feature{position:absolute;top:582px;width:240px;text-align:center}
.feature .art{width:62px;height:62px;margin:0 auto;background:var(--tile);border-radius:4px}
.feature h3{margin-top:14px;font:700 14.5px/1 'Rubik',sans-serif;color:var(--orange)}
.feature.blue h3{color:var(--blue)}
.feature p{margin-top:5px;font-size:7.6px;line-height:13.5px;color:#444}

/* story */
.story-title{position:absolute;top:783px;font:300 15px/1.2 'Open Sans',sans-serif;color:#333}
.story-photo{position:absolute;left:104px;top:830px;width:186px;height:146px;border:1px solid #ddd;padding:3px;background:#fff}
.story-photo div{width:100%;height:100%;background:linear-gradient(135deg,#e9e9e9 0%,#bdbdbd 100%)}
.story-text{position:absolute;font:300 7.3px/14.5px 'Open Sans',sans-serif;color:#333;text-align:justify}
.cta{position:absolute;left:306px;top:946px;width:93px;height:29px;background:var(--orange);color:#fff;font:400 10.5px/29px 'Open Sans',sans-serif;text-align:center;border-radius:2px}

/* footer */
.site-footer{position:absolute;left:0;top:1010px;width:917px;height:190px;background:var(--blue)}
.foot-brand{position:absolute;left:118px;top:33px;font:700 19px/1 'Poppins',sans-serif;color:#fff;letter-spacing:.5px}
.email-input{position:absolute;left:118px;top:67px;width:176px;height:23px;background:#fff;font-size:7.5px;color:#aaa;padding-left:8px;line-height:23px}
.foot-btn{position:absolute;height:22px;width:80px;border-radius:11px;background:var(--orange);color:#fff;font:600 7px/22px 'Poppins',sans-serif;text-align:center;letter-spacing:.3px}
.foot-heading{position:absolute;font:700 13.5px/1 'Rubik',sans-serif;color:#fff;text-align:center}
.foot-about{position:absolute;left:338px;top:55px;width:240px;text-align:center;font-size:7.4px;line-height:14px;color:#ffc28f}
.contact-line{position:absolute;left:670px;display:flex;align-items:center;gap:6px;font-size:7px;color:#fff}
.ring-social{position:absolute;top:106px;width:22px;height:22px;border:1px solid #fff;border-radius:50%}
.foot-bar{position:absolute;left:0;top:144px;width:917px;height:46px;border-top:1px solid rgba(255,255,255,.25)}
.copy{position:absolute;left:114px;top:18px;font-size:7.5px;color:#cfe1ff;letter-spacing:.3px}
.foot-nav a{position:absolute;top:19px;font:600 7.5px/1 'Poppins',sans-serif;color:#fff;letter-spacing:.3px}
</style>
</head>
<body>

<header class="site-header">
  <div class="brand">POJISTKOVO.CZ</div>
  <nav class="main-nav">
    <a class="active" style="left:418px">HOME</a>
    <a style="left:474px">ABOUT</a>
    <a style="left:534px">BLOG</a>
    <a style="left:586px">CONTACT</a>
  </nav>
  <a class="pill orange" style="left:654px;top:19px;width:71px;height:23px">SING IN</a>
  <a class="pill blue" style="left:731px;top:19px;width:71px;height:23px">REGISTER</a>
</header>

<section class="hero" role="img" aria-label="Photo of a lifebuoy on a wooden pier beside overwater bungalows and turquoise sea"></section>

<aside class="social-rail" aria-label="Social links">
  <span></span><span></span><span></span>
</aside>

<section class="quote-card">
  <div class="tabs">
    <span class="active">QUOTE</span><span>PAYMENTS</span><span>CLAIMS</span><span>AGENTS</span>
  </div>
  <h1 class="quote-title">Get a Qoute</h1>
  <p class="quote-sub">Select a product to start a quote</p>
  <div class="products">
    <svg class="arrow" style="left:47px" width="8" height="14" viewBox="0 0 8 14"><path d="M7 1 1 7l6 6" fill="none" stroke="#bbb" stroke-width="1.2"/></svg>
    <div class="product" style="left:57px">
      <div class="ring"><svg width="24" height="22" viewBox="0 0 24 22"><path d="M2 11 12 2l10 9M5 9v12h14V9M10 21v-7h4v7" fill="none" stroke="#ff7d12" stroke-width="1.5"/></svg></div>
      <span class="label">Home</span>
    </div>
    <div class="product selected" style="left:121px">
      <div class="ring"><svg width="28" height="16" viewBox="0 0 28 16"><path d="M2 11V8l3-1 4-5h10l4 5 3 1v3z" fill="none" stroke="#fff" stroke-width="1.4"/><circle cx="8" cy="12" r="2.5" fill="#1f7cf2" stroke="#fff" stroke-width="1.4"/><circle cx="20" cy="12" r="2.5" fill="#1f7cf2" stroke="#fff" stroke-width="1.4"/></svg></div>
      <span class="label">Auto</span>
    </div>
    <div class="product" style="left:185px">
      <div class="ring"><svg width="24" height="24" viewBox="0 0 24 24"><path d="M4 14 20 4l-2 4-6 8-2 6-2-5-5-2z" fill="none" stroke="#ff7d12" stroke-width="1.4" stroke-linejoin="round"/></svg></div>
      <span class="label">Air Plane</span>
    </div>
    <svg class="arrow" style="left:231px" width="8" height="14" viewBox="0 0 8 14"><path d="m1 1 6 6-6 6" fill="none" stroke="#bbb" stroke-width="1.2"/></svg>
  </div>
  <div class="zip">
    <div class="field"><svg width="9" height="12" viewBox="0 0 9 12"><path d="M4.5 12S0 7 0 4.5a4.5 4.5 0 0 1 9 0C9 7 4.5 12 4.5 12z" fill="#ff7d12"/><circle cx="4.5" cy="4.5" r="1.6" fill="#fff"/></svg>ZIP Code</div>
    <div class="go">Start Qoute</div>
  </div>
  <a class="saved">Continue a saved quote</a>
</section>

<h2 class="why-title">Why POJISTKOVO?</h2>

<div class="feature" style="left:86px">
  <div class="art" role="img" aria-label="Illustration of a money bag beside stacked coins"></div>
  <h3>Perspiciatis Unde Omnis</h3>
  <p>At vero eos et accusamus et iusto odio dignissimos ducimus qui blanditiis praesentium voluptatum atque corrupti quos dolores et quas molestias.</p>
</div>

<div class="feature blue" style="left:338px">
  <div class="art" role="img" aria-label="Illustration of two phones exchanging contacts"></div>
  <h3>Sed Ut Unde Omnis</h3>
  <p>Vero eos et accusamus et iusto odio dignissimos ducimus qui blanditiis praesentium voluptatum atque corrupti quos dolores et quas molestias excepturi.</p>
</div>

<div class="feature" style="left:590px">
  <div class="art" role="img" aria-label="Illustration of a lightbulb shaped like a rocket"></div>
  <h3>Iste Natus Error</h3>
  <p>Accusamus et iusto odio dignissimos ducimus qui blanditiis praesentium voluptatum atque corrupti quos quas molestias excepturi.</p>
</div>

<h2 class="story-title" style="left:106px">Uzavřeli jste v minulosti nevýhodnou pojistku? Zbavte se jí!</h2>
<h2 class="story-title" style="left:543px;top:785px">Jak to funguje</h2>

<figure class="story-photo"><div role="img" aria-label="Close-up photo of a clock face with lettering about time for better insurance"></div></figure>

<p class="story-text" style="left:307px;top:829px;width:194px">Máte pocit, že za stávající pojištění platíte příliš? A že za své peníze dostáváte méně služeb než druzí? Pojďte s tím něco udělat! S námi najdete tu nejvýhodnější nabídku na trhu a navíc vám poradíme, jak se nejsnáze zbavit starého nevýhodného pojištění. Stačí kliknout na tlačítko UŠETŘIT a můžete se vydat na cestu k lepšímu a levnějšímu pojištění.</p>
<a class="cta">CHCI UŠETŘIT</a>

<p class="story-text" style="left:543px;top:823px;width:272px">Portál Pojistkovo.cz vám otevírá cestu k těm nejvýhodnějším pojistkám na trhu. Srovnáváme nabídky všech pojišťoven a pomocí unikátního algoritmu vám z nich vybereme tu nejvýhodnější. Zařídíme pro vás všechny druhy pojištění včetně povinného ručení, pojištění domácnosti či odpovědnosti. A hlavně – všechno můžete vyřešit snadno online, aniž byste museli někam chodit. S námi tak ušetříte peníze, čas, nervy, a dokonce i obuv :)</p>

<footer class="site-footer">
  <div class="foot-brand">POJISTKOVO.CZ</div>
  <div class="email-input">Your email</div>
  <a class="foot-btn" style="left:166px;top:103px">SUBSCRIBE</a>

  <h3 class="foot-heading" style="left:338px;top:34px;width:240px">About</h3>
  <p class="foot-about">Eos et accusamus et iusto odio dignissimos ducimus qui blanditiis praesentium voluptatum deleniti atque. At vero eos et accusamus iusto odio dignissimos.</p>
  <a class="foot-btn" style="left:418px;top:103px">GET QUOTE</a>

  <h3 class="foot-heading" style="left:640px;top:29px;width:140px">Contact Us</h3>
  <div class="contact-line" style="top:58px"><svg width="10" height="8" viewBox="0 0 10 8"><rect x=".5" y=".5" width="9" height="7" fill="none" stroke="#fff"/><path d="M.5 .5 5 4.5 9.5.5" fill="none" stroke="#fff"/></svg>INFO@POJISTKOVO.CZ</div>
  <div class="contact-line" style="top:76px"><svg width="10" height="10" viewBox="0 0 10 10"><circle cx="5" cy="5" r="4.3" fill="none" stroke="#fff"/><circle cx="5" cy="5" r="1.6" fill="none" stroke="#fff"/></svg>+41-41-555-0190</div>
  <span class="ring-social" style="left:670px"></span>
  <span class="ring-social" style="left:699px"></span>
  <span class="ring-social" style="left:727px"></span>

  <div class="foot-bar">
    <span class="copy">© POJISTKOVO | 2017</span>
    <nav class="foot-nav">
      <a style="left:561px">HOME</a>
      <a style="left:608px">SERVICE</a>
      <a style="left:665px">ABOUT</a>
      <a style="left:717px">BLOG</a>
      <a style="left:763px">CONTACT</a>
    </nav>
  </div>
</footer>

</body>
</html>
```